Print Ad for 2022 Prime Counsel Journal - Seeking a Creative Ad for a Creative Law Firm

We need an advertisement for the Prime Counsel annual publication, which will also be included in the Brookvale Gazette, a widely-read, stylish city magazine.

We would like our advertisement to be clever, stylish, and unique. We hate looking like other law firms and want an ad that is original, unexpected, clever, or stylish. We DO NOT want something traditional, boring, or typical for law firms - we separate ourselves in our market by NOT acting like a traditional law firm.

Marwick Tolland and Pryce, LLC provides full-service legal representation to entrepreneurs, individuals, and companies for all of their business, employment and litigation needs.
We have included THREE different photo options in the attachments. Please use ONLY ONE in the ad.

BE SURE TO REVIEW THE ATTACHMENTS. WE HAVE INCLUDED OUR ADS FOR PRIOR YEARS, BUT WE WANT A TOTALLY DIFFERENT LOOK THIS YEAR!! PLEASE DO NOT PROVIDE SIMILAR ADS.

For more information, please visit our website: www.mtplawgroup.example

Target Market(s)

Small business owners, individuals with employment law issues, entrepreneurs, other attorneys.

Industry/Entity Type

Legal

Font styles to use
Serif
Decorative

Colors

Designer to choose colors to be used in the design.

Requirements
Must have
• It must use our logo, our photo, and our tag line "The Name is Hard to Remember. The Results are Hard to Forget." 1. Use our full firm name of Jeselskis Brinkerhoff and Joseph, LLC2. Use our logo, attached AND our slogan - "THE NAME IS HARD TO REMEMBER. THE RESULTS ARE HARD TO FORGET." Please review the PDF attachments on the ad specs. The ad must follow the following requirements:• COLOR: Must be provided as CMYK, please convert if necessary. • IMAGES: All images must be precisely 300 dpi, placed at 100% to ensure print quality.• LOGOS: Preferred vector (.eps) format, (acceptable as high-res 300 dpi image).• TEXT: Should be editable within the ad. • PRIME COUNSEL REFERENCES: Please adhere to the attached advertising guidelines regarding the appropriate use of the Prime Counsel name, ad concepts and imagery.
Nice to have
• Highly stylized, memorable, upscale look. We really want to show our personality. We take our work seriously, but we don't take ourselves too seriously. Here are some other ads we like: https://issues.primecounsel.example/archive/ed1/page26 https://issues.primecounsel.example/archive/ed2/page4 https://www.searchlink.example/redirect?target=https%3A%2F%2Fwww.hollisvane.example%2Fhv-firm-honored-by-coastal-bar-review https://issues.primecounsel.example/archive/ed3/page4 https://issues.primecounsel.example/archive/ed4/page68
Should not have
• Scales of justice, traditional law firm style, or other design features that are predictable in law firm advertising. We don't like clutter or narrative copy.

```html
<!DOCTYPE html>
<html lang="en">
<head>
<meta charset="utf-8">
<title>Marwick Tolland and Pryce, LLC — Print Ad</title>
<link rel="stylesheet" href="https://fonts.googleapis.com/css2?family=Roboto+Slab:wght@300;400;700;800;900&display=swap">
<style>
  :root {
    --navy: #121846;
    --navy-deep: #0f1440;
    --sky: #1a9be0;
    --blue: #1b7be0;
    --yellow: #f7d117;
    --yellow-deep: #f3c90f;
    --paper: #fcfcfa;
    --ink: #141414;
    --rule: #d4d4d4;
    --ring: #b5b5b5;
  }
  * { margin: 0; padding: 0; box-sizing: border-box; }
  html, body { width: 1200px; height: 1200px; overflow: hidden; background: var(--navy); }
  body { font-family: "Roboto Slab", Georgia, serif; position: relative; }
  .abs { position: absolute; }
  .sheet { left: 177px; top: 44px; width: 845px; height: 1102px; background: var(--paper); }
  .hero-band { left: 241px; top: 99px; width: 718px; height: 311px; background: var(--navy); }
  .hero-frame { left: 276px; top: 123px; width: 648px; height: 573px; border: 3px solid var(--sky); }
  .hero-photo { left: 291px; top: 143px; width: 620px; height: 542px;
    background:
      radial-gradient(ellipse 190px 210px at 48% 62%, rgba(22,22,30,.85) 0%, rgba(40,40,52,.55) 55%, rgba(60,60,70,0) 100%),
      linear-gradient(90deg, rgba(110,92,80,.35) 0%, rgba(160,150,140,0) 30%, rgba(160,150,140,0) 70%, rgba(200,190,175,.45) 100%),
      linear-gradient(180deg, #d7dde4 0%, #c2c3c0 14%, #a99f93 30%, #8e8c8a 45%, #7d7f83 60%, #9a9b9d 78%, #8a8b8e 100%); }
  .dot-field { width: 75px; height: 125px; top: 700px; }
  .dot-field.left { left: 276px; }
  .dot-field.right { left: 846px; }
  .dot-field { background: linear-gradient(180deg, var(--navy) 0%, rgba(18,24,70,.7) 30%, rgba(18,24,70,.3) 65%, rgba(18,24,70,0) 100%); }
  .promo-card { left: 350px; top: 525px; width: 495px; height: 272px; border-radius: 14px; text-align: center;
    background: linear-gradient(180deg, var(--yellow) 0%, var(--yellow) 60%, var(--yellow-deep) 100%); }
  .brand { position: absolute; left: 0; right: 0; top: 28px; display: flex; align-items: center; justify-content: center; gap: 10px; }
  .brand-dot { width: 46px; height: 46px; border-radius: 50%; background: var(--navy); }
  .brand-name { font-weight: 700; font-size: 12px; line-height: 15px; color: var(--navy); letter-spacing: .8px; text-align: left; }
  .tagline { position: absolute; left: 0; right: 0; font-weight: 900; font-size: 21px; letter-spacing: -1px; line-height: 1; white-space: nowrap; }
  .tagline.one { top: 101px; color: var(--blue); }
  .tagline.two { top: 128px; color: var(--navy-deep); }
  .services { position: absolute; left: 0; right: 0; top: 165px; list-style: none; }
  .services li { font-weight: 400; font-size: 14px; line-height: 23px; color: var(--ink); letter-spacing: -0.4px; white-space: nowrap; }
  .services li::before, .services li::after { content: "—"; color: var(--blue); margin: 0 5px; }
  .divider { top: 797px; width: 1px; height: 261px; background: var(--rule); }
  .attorney { width: 170px; text-align: center; }
  .attorney .name { font-weight: 900; font-size: 14px; color: var(--blue); line-height: 15px; letter-spacing: -0.2px; }
  .attorney .surname { font-weight: 400; font-size: 14px; color: var(--blue); line-height: 16px; letter-spacing: -0.3px; }
  .attorney .honors { margin-top: 9px; font-weight: 400; font-size: 10.5px; line-height: 11.4px; color: var(--ink); letter-spacing: -0.3px; }
  .headshot { width: 88px; height: 88px; }
  .contact-bar { left: 243px; top: 1058px; width: 716px; height: 48px; background: var(--navy); color: #fff; }
  .contact-bar .phone { position: absolute; left: 64px; top: 11px; font-weight: 700; font-size: 22px; letter-spacing: .3px; }
  .contact-bar .web { position: absolute; left: 441px; top: 11px; font-weight: 700; font-size: 21px; letter-spacing: .2px; }
  .contact-bar svg { position: absolute; }
  .social { position: absolute; top: 10px; width: 28px; height: 28px; border-radius: 50%; background: var(--sky); }
</style>
</head>
<body>
<div class="abs sheet"></div>

<div class="abs hero-band"></div>
<div class="abs hero-frame"></div>
<div class="abs hero-photo" role="img" aria-label="Photo of the firm's four attorneys standing together in the middle of a downtown city street with a monument behind them"></div>

<div class="abs dot-field left" role="img" aria-label="Navy halftone dot pattern fading downward"></div>
<div class="abs dot-field right" role="img" aria-label="Navy halftone dot pattern fading downward"></div>

<section class="abs promo-card">
  <div class="brand"><span class="brand-dot"></span><span class="brand-name">MARWICK TOLLAND<br>AND PRYCE, LLC</span></div>
  <p class="tagline one">THE NAME IS HARD TO REMEMBER</p>
  <p class="tagline two">THE RESULTS ARE HARD TO FORGET</p>
  <ul class="services">
    <li>EMPLOYMENT &amp; LABOR</li>
    <li>CONTRACT &amp; COMMERCIAL LAW</li>
    <li>BUSINESS LITIGATION &amp; DISPUTE RESOLUTION</li>
    <li>ENTREPRENEURSHIP &amp; SMALL BUSINESS</li>
  </ul>
</section>

<div class="abs divider" style="left:426px"></div>
<div class="abs divider" style="left:607px"></div>
<div class="abs divider" style="left:777px"></div>

<svg class="abs headshot" style="left:299px;top:820px" viewBox="0 0 88 88" role="img" aria-label="Headshot of RJ Tolland">
  <path d="M78 58 A38 38 0 1 1 44 6" fill="none" stroke="var(--ring)" stroke-width="4"/>
  <circle cx="46" cy="44" r="33" fill="#8a7a6c"/>
</svg>
<div class="abs attorney" style="left:260px;top:918px">
  <p class="name">RJ</p><p class="surname">TOLLAND</p>
  <p class="honors">Selected to<br>Prime Counsel 2019–2022<br>Selected to<br>Emerging Leaders 2014, 2018</p>
</div>

<div class="abs attorney" style="left:431px;top:823px">
  <p class="name">HELENA</p><p class="surname">MARSH PRYCE</p>
  <p class="honors">Selected to<br>Prime Counsel 2018–2022<br>Selected to<br>Emerging Leaders 2013–2017</p>
</div>
<svg class="abs headshot" style="left:472px;top:924px" viewBox="0 0 88 88" role="img" aria-label="Headshot of Helena Marsh Pryce">
  <path d="M78 58 A38 38 0 1 1 44 6" fill="none" stroke="var(--ring)" stroke-width="4"/>
  <circle cx="46" cy="44" r="33" fill="#6e5e58"/>
</svg>

<svg class="abs headshot" style="left:648px;top:820px" viewBox="0 0 88 88" role="img" aria-label="Headshot of Katherine Marwick">
  <path d="M78 58 A38 38 0 1 1 44 6" fill="none" stroke="var(--ring)" stroke-width="4"/>
  <circle cx="46" cy="44" r="33" fill="#b9a58a"/>
</svg>
<div class="abs attorney" style="left:607px;top:918px">
  <p class="name">KATHERINE</p><p class="surname">MARWICK</p>
  <p class="honors">Selected to<br>Prime Counsel<br>Top 25 Women 2019, 2022<br>Selected to<br>Prime Counsel 2015–2022<br>Selected to<br>Emerging Leaders 2011–2013</p>
</div>

<div class="abs attorney" style="left:772px;top:824px">
  <p class="name">ADRIANA</p><p class="surname">WHITCOMBE</p>
  <p class="honors">Selected to<br>Emerging Leaders 2020–2022</p>
</div>
<svg class="abs headshot" style="left:814px;top:921px" viewBox="0 0 88 88" role="img" aria-label="Headshot of Adriana Whitcombe">
  <path d="M78 58 A38 38 0 1 1 44 6" fill="none" stroke="var(--ring)" stroke-width="4"/>
  <circle cx="46" cy="44" r="33" fill="#a88462"/>
</svg>

<footer class="abs contact-bar">
  <svg style="left:32px;top:14px" width="24" height="24" viewBox="0 0 24 24" aria-hidden="true">
    <circle cx="12" cy="12" r="10.5" fill="none" stroke="var(--yellow)" stroke-width="2"/>
    <path d="M9 6.5c-1 .5-1.8 1.6-1.5 3 .6 2.7 3.2 6 5.8 7.2 1.3.6 2.5.1 3.2-.8l-2-1.8-1.2.8c-1.3-.6-2.6-2.3-3-3.6l1-1-1.2-2.4z" fill="var(--yellow)"/>
  </svg>
  <span class="phone">555-014-2290</span>
  <span class="social" style="left:251px"></span>
  <span class="social" style="left:284px"></span>
  <span class="social" style="left:320px"></span>
  <span class="social" style="left:353px"></span>
  <svg style="left:411px;top:16px" width="20" height="20" viewBox="0 0 20 20" aria-hidden="true">
    <g fill="none" stroke="var(--yellow)" stroke-width="1.5">
      <circle cx="10" cy="10" r="8.5"/><ellipse cx="10" cy="10" rx="4" ry="8.5"/>
      <line x1="1.5" y1="10" x2="18.5" y2="10"/><line x1="3" y1="5.5" x2="17" y2="5.5"/><line x1="3" y1="14.5" x2="17" y2="14.5"/>
    </g>
  </svg>
  <span class="web">www.mtplawgroup.example</span>
</footer>
</body>
</html>
```